Corporate Power Point Template

Tarrowmead Group, Inc. produces and sells ready-mixed concrete, aggregates, and concrete-related products and services for the construction industry in the United States.

We are looking for a simple and sleek design that will look great on a projector, as well as when printed on paper. We prefer a lighter background color that will not waste ink when printed. We would also like to stay away from wavy banners, or over-the-top graphics that take away from usable space in the deck. Please use a variation of the color scheme in the "Brand Standards" file attached.

```html
<!DOCTYPE html>
<html lang="en">
<head>
<meta charset="utf-8">
<title>Tarrowmead Group, Inc. – Corporate Presentation Template</title>
<link href="https://fonts.googleapis.com/css2?family=Montserrat:wght@400;600;700;800&display=swap" rel="stylesheet">
<style>
  :root{
    --brand-red:#c8102e;
    --brand-red-dark:#9e0c22;
    --ink:#3c3c3c;
    --ink-soft:#7a7a7a;
    --rule:#d9d9d9;
    --panel:#f1f1f1;
    --paper:#ffffff;
    --stage:#9a9a9a;
    --photo-sky:#8fa6bd;
    --photo-steel:#4f6478;
  }
  *{box-sizing:border-box;margin:0;padding:0}
  html,body{width:835px;height:1200px;overflow:hidden}
  body{background:var(--stage);font-family:"Montserrat",Arial,sans-serif;color:var(--ink)}
  .deck{position:relative;width:835px;height:1200px;
    display:grid;grid-template-columns:repeat(3,222px);grid-template-rows:repeat(6,167px);
    column-gap:28px;row-gap:25px;padding:36px 0 0 56px}
  .slide{position:relative;background:var(--paper);overflow:hidden;box-shadow:0 1px 3px rgba(0,0,0,.25)}
  .abs{position:absolute}
  .red{background:var(--brand-red)}
  .red-dark{background:var(--brand-red-dark)}
  .panel{background:var(--panel)}
  .photo{background:linear-gradient(135deg,var(--photo-sky),var(--photo-steel))}
  .photo-warm{background:linear-gradient(135deg,#c9b8a6,#6d5f55)}
  .photo-red{background:linear-gradient(135deg,#d64a5c,#7a0d1d)}
  .title{font-weight:700;font-size:7px;letter-spacing:.4px;color:var(--brand-red);text-transform:uppercase}
  .title.on-red{color:#fff}
  .body{font-size:5px;line-height:1.5;color:var(--ink-soft)}
  .body.on-red{color:#fbe3e6}
  .label{font-size:5px;font-weight:600;color:var(--ink)}
  .icon{width:12px;height:12px;border-radius:50%;background:var(--brand-red)}
  .icon-sq{width:14px;height:14px;background:var(--brand-red)}
  .wordmark{font-weight:800;color:var(--brand-red);font-size:11px;line-height:1.15}
  table.data{border-collapse:collapse;font-size:5px;width:100%}
  table.data th{background:var(--brand-red);color:#fff;font-weight:600;padding:3px}
  table.data td{border-bottom:1px solid var(--rule);padding:3px;text-align:center;color:var(--ink-soft)}
</style>
</head>
<body>
<main class="deck">

  <!-- 1 cover -->
  <section class="slide cover">
    <div class="abs" style="left:16px;top:50px;display:flex;align-items:center;gap:5px">
      <span style="width:10px;height:10px;background:var(--brand-red)"></span>
      <span class="wordmark">Tarrowmead<br>Group, Inc.</span>
    </div>
    <div class="abs photo" style="left:111px;top:0;width:111px;height:150px" role="img" aria-label="Modern glass office towers"></div>
    <div class="abs red" style="left:0;bottom:0;width:222px;height:17px"></div>
  </section>

  <!-- 2 introduction -->
  <section class="slide intro">
    <div class="abs red" style="left:0;top:0;width:86px;height:167px"></div>
    <p class="abs title on-red" style="left:10px;top:14px">Introduction</p>
    <div class="abs" style="left:100px;top:14px;display:flex;align-items:center;gap:3px">
      <span style="width:6px;height:6px;background:var(--brand-red)"></span>
      <span style="font-size:5px;font-weight:700;color:var(--brand-red)">Tarrowmead Group, Inc.</span>
    </div>
    <p class="abs body" style="left:100px;top:36px;width:110px">Our crews deliver concrete on time across the country.</p>
    <p class="abs body" style="left:100px;top:70px;width:110px">We build lasting value for every partner.</p>
  </section>

  <!-- 3 team -->
  <section class="slide team">
    <p class="abs title" style="left:0;width:222px;text-align:center;top:10px">Lorem ipsum dolor</p>
    <div class="abs red" style="left:0;top:70px;width:222px;height:97px"></div>
    <div class="abs" style="left:20px;top:30px;width:182px;display:flex;justify-content:space-between">
      <div style="width:46px;height:46px;border-radius:50%;border:3px solid #fff" class="photo-warm" role="img" aria-label="Team member portrait"></div>
      <div style="width:46px;height:46px;border-radius:50%;border:3px solid #fff" class="photo-warm" role="img" aria-label="Team member portrait"></div>
      <div style="width:46px;height:46px;border-radius:50%;border:3px solid #fff" class="photo-warm" role="img" aria-label="Team member portrait"></div>
    </div>
    <div class="abs" style="left:20px;top:84px;width:182px;display:flex;justify-content:space-between;font-size:5px;color:#fff;font-weight:600">
      <span style="width:46px;text-align:center">Ana Ruiz</span>
      <span style="width:46px;text-align:center">Mark Dale</span>
      <span style="width:46px;text-align:center">Lena Voss</span>
    </div>
  </section>

  <!-- 4 icon grid -->
  <section class="slide features">
    <p class="abs title" style="left:0;width:222px;text-align:center;top:14px">Lorem ipsum dolor</p>
    <div class="abs" style="left:24px;top:44px;width:176px;display:grid;grid-template-columns:repeat(3,1fr);row-gap:26px">
      <div style="display:flex;gap:4px;align-items:center"><span class="icon"></span><span class="label">Quality</span></div>
      <div style="display:flex;gap:4px;align-items:center"><span class="icon"></span><span class="label">Safety</span></div>
      <div style="display:flex;gap:4px;align-items:center"><span class="icon"></span><span class="label">Delivery</span></div>
      <div style="display:flex;gap:4px;align-items:center"><span class="icon"></span><span class="label">Service</span></div>
      <div style="display:flex;gap:4px;align-items:center"><span class="icon"></span><span class="label">Growth</span></div>
      <div style="display:flex;gap:4px;align-items:center"><span class="icon"></span><span class="label">Value</span></div>
    </div>
  </section>

  <!-- 5 photo + red column + icon list -->
  <section class="slide split">
    <div class="abs photo-red" style="left:0;top:0;width:70px;height:167px" role="img" aria-label="Construction site with red overlay"></div>
    <div class="abs red" style="left:70px;top:0;width:70px;height:167px"></div>
    <p class="abs title on-red" style="left:78px;top:20px;width:56px">Lorem ipsum dolor</p>
    <p class="abs body on-red" style="left:78px;top:50px;width:56px">Strong mixes for every job site.</p>
    <div class="abs" style="left:152px;top:30px;display:flex;flex-direction:column;gap:22px">
      <div style="display:flex;gap:4px;align-items:center"><span class="icon-sq"></span><span class="label">Plants</span></div>
      <div style="display:flex;gap:4px;align-items:center"><span class="icon-sq"></span><span class="label">Fleet</span></div>
      <div style="display:flex;gap:4px;align-items:center"><span class="icon-sq"></span><span class="label">Labs</span></div>
    </div>
  </section>

  <!-- 6 leadership -->
  <section class="slide leadership">
    <div class="abs photo" style="left:100px;top:0;width:122px;height:120px" role="img" aria-label="Business people in suits"></div>
    <p class="abs title" style="left:12px;top:26px;width:80px">Lorem ipsum dolor</p>
    <p class="abs body" style="left:12px;top:48px;width:80px">Experienced people guiding steady growth.</p>
    <div class="abs red" style="left:0;top:120px;width:222px;height:47px"></div>
    <p class="abs title on-red" style="left:110px;top:138px">Lorem ipsum dolor</p>
  </section>

  <!-- 7 mobile -->
  <section class="slide mobile">
    <p class="abs title" style="left:12px;top:10px">Lorem ipsum dolor sit amet</p>
    <div class="abs photo" style="left:12px;top:28px;width:90px;height:60px" role="img" aria-label="Hand holding a phone"></div>
    <p class="abs body" style="left:110px;top:36px;width:100px">Mobile ordering for every crew.</p>
    <div class="abs" style="left:12px;top:98px;width:198px;display:flex;gap:6px">
      <div class="photo-warm" style="flex:1;height:58px" role="img" aria-label="Team at work"></div>
      <div class="photo" style="flex:1;height:58px" role="img" aria-label="Office meeting"></div>
      <div class="photo-warm" style="flex:1;height:58px" role="img" aria-label="Site engineers"></div>
    </div>
  </section>

  <!-- 8 quality -->
  <section class="slide quality">
    <div class="abs" style="left:0;top:0;width:222px;height:30px;background:#3a3f47"></div>
    <p class="abs title on-red" style="left:0;width:222px;text-align:center;top:11px;font-size:5.5px">Lorem ipsum dolor sit amet consectetur</p>
    <div class="abs photo" style="left:12px;top:42px;width:100px;height:110px" role="img" aria-label="Colleagues at a laptop"></div>
    <p class="abs title" style="left:124px;top:60px">Quality</p>
    <div class="abs red" style="left:124px;top:72px;width:20px;height:2px"></div>
    <p class="abs body" style="left:124px;top:80px;width:86px">Tested mixes meet every spec.</p>
  </section>

  <!-- 9 red statement -->
  <section class="slide statement red">
    <div class="abs red-dark" style="left:0;top:0;width:222px;height:8px"></div>
    <p class="abs title on-red" style="left:0;width:222px;text-align:center;top:36px;font-size:9px;line-height:1.4">Lorem ipsum dolor sit amet<br>consectetur adipiscing elit</p>
    <div class="abs" style="left:36px;top:98px;width:150px;display:flex;justify-content:space-between">
      <div style="text-align:center"><span style="display:block;width:14px;height:14px;border:1.5px solid #fff;margin:0 auto 4px"></span><span style="font-size:5px;color:#fff">Build</span></div>
      <div style="text-align:center"><span style="display:block;width:14px;height:14px;border:1.5px solid #fff;margin:0 auto 4px"></span><span style="font-size:5px;color:#fff">Plan</span></div>
      <div style="text-align:center"><span style="display:block;width:14px;height:14px;border:1.5px solid #fff;margin:0 auto 4px"></span><span style="font-size:5px;color:#fff">Grow</span></div>
    </div>
  </section>

  <!-- 10 list with image -->
  <section class="slide products">
    <div class="abs" style="left:14px;top:22px;display:flex;flex-direction:column;gap:12px">
      <div style="display:flex;gap:6px;align-items:center"><span style="width:18px;height:18px;background:#6b6b6b"></span><span class="label">Aggregates</span></div>
      <div style="display:flex;gap:6px;align-items:center"><span style="width:18px;height:18px;background:#6b6b6b"></span><span class="label">Ready mix</span></div>
      <div style="display:flex;gap:6px;align-items:center"><span style="width:18px;height:18px;background:#6b6b6b"></span><span class="label">Precast</span></div>
      <div style="display:flex;gap:6px;align-items:center"><span style="width:18px;height:18px;background:var(--brand-red)"></span><span class="label">Transport</span></div>
    </div>
    <div class="abs photo" style="left:118px;top:22px;width:90px;height:120px" role="img" aria-label="Hand on a tablet"></div>
  </section>

  <!-- 11 two columns -->
  <section class="slide columns">
    <p class="abs title" style="left:0;width:222px;text-align:center;top:12px">Lorem ipsum dolor</p>
    <div class="abs" style="left:14px;top:30px;width:194px;display:flex;gap:8px">
      <div style="flex:1">
        <div class="red" style="height:14px"></div>
        <div class="panel" style="height:40px;padding:5px"><p class="body">Clear plans for each project.</p></div>
      </div>
      <div style="flex:1">
        <div style="height:14px;background:#6b6b6b"></div>
        <div class="panel" style="height:40px;padding:5px"><p class="body">Clear plans for each project.</p></div>
      </div>
    </div>
  </section>

  <!-- 12 table -->
  <section class="slide table">
    <p class="abs title" style="left:0;width:222px;text-align:center;top:12px">Lorem ipsum dolor</p>
    <div class="abs" style="left:14px;top:30px;width:194px">
      <table class="data">
        <tr><th>Item</th><th>2019</th><th>2020</th><th>2021</th></tr>
        <tr><td>01</td><td>12</td><td>18</td><td>24</td></tr>
        <tr><td>02</td><td>15</td><td>21</td><td>27</td></tr>
        <tr><td>03</td><td>10</td><td>16</td><td>22</td></tr>
        <tr><td>04</td><td>14</td><td>19</td><td>25</td></tr>
        <tr><td>05</td><td>11</td><td>17</td><td>23</td></tr>
      </table>
    </div>
  </section>

  <!-- 13 flowchart -->
  <section class="slide flow">
    <svg class="abs" style="left:0;top:0" width="222" height="167" viewBox="0 0 222 167">
      <g stroke="#9a9a9a" stroke-width="1" fill="none">
        <path d="M52 40 H80 M80 40 V110 M80 58 H100 M80 84 H100 M80 110 H100 M144 58 H160 M144 84 H160"/>
      </g>
    </svg>
    <div class="abs red" style="left:14px;top:33px;width:38px;height:14px;font-size:5px;color:#fff;display:flex;align-items:center;justify-content:center">Plan</div>
    <div class="abs red" style="left:100px;top:51px;width:44px;height:14px;font-size:5px;color:#fff;display:flex;align-items:center;justify-content:center">Mix</div>
    <div class="abs red" style="left:100px;top:77px;width:44px;height:14px;font-size:5px;color:#fff;display:flex;align-items:center;justify-content:center">Pour</div>
    <div class="abs red" style="left:100px;top:103px;width:44px;height:14px;font-size:5px;color:#fff;display:flex;align-items:center;justify-content:center">Cure</div>
    <div class="abs panel" style="left:160px;top:51px;width:44px;height:14px;font-size:5px;display:flex;align-items:center;justify-content:center">Test</div>
    <div class="abs panel" style="left:160px;top:77px;width:44px;height:14px"></div>
  </section>

  <!-- 14 teamwork -->
  <section class="slide teamwork">
    <div class="abs red" style="left:0;top:0;width:222px;height:26px"></div>
    <p class="abs title on-red" style="left:0;width:222px;text-align:center;top:10px">Lorem ipsum dolor</p>
    <div class="abs photo-warm" style="left:14px;top:36px;width:120px;height:118px" role="img" aria-label="Team hands joined together"></div>
    <p class="abs body" style="left:144px;top:50px;width:66px">Partners working side by side.</p>
  </section>

  <!-- 15 process icons -->
  <section class="slide process">
    <p class="abs title" style="left:0;width:222px;text-align:center;top:12px">Lorem ipsum dolor sit amet</p>
    <div class="abs" style="left:24px;top:36px;display:flex;flex-direction:column;gap:10px">
      <div style="display:flex;align-items:center;gap:6px"><span class="icon"></span><span style="width:40px;height:16px" class="panel"></span><span style="width:0;height:0;border-left:5px solid var(--brand-red);border-top:4px solid transparent;border-bottom:4px solid transparent"></span><span style="width:58px;height:16px;background:#6b6b6b;font-size:5px;color:#fff;display:flex;align-items:center;justify-content:center">Order</span></div>
      <div style="display:flex;align-items:center;gap:6px"><span class="icon"></span><span style="width:40px;height:16px" class="panel"></span><span style="width:0;height:0;border-left:5px solid var(--brand-red);border-top:4px solid transparent;border-bottom:4px solid transparent"></span><span style="width:58px;height:16px;background:var(--brand-red);font-size:5px;color:#fff;display:flex;align-items:center;justify-content:center">Deliver</span></div>
      <div style="display:flex;align-items:center;gap:6px"><span class="icon"></span><span style="width:40px;height:16px" class="panel"></span><span style="width:0;height:0;border-left:5px solid var(--brand-red);border-top:4px solid transparent;border-bottom:4px solid transparent"></span><span style="width:58px;height:16px;background:#6b6b6b;font-size:5px;color:#fff;display:flex;align-items:center;justify-content:center">Review</span></div>
    </div>
  </section>

  <!-- 16 services -->
  <section class="slide services">
    <p class="abs title" style="left:14px;top:12px">Our services</p>
    <div class="abs" style="left:14px;top:30px;width:194px;display:flex;gap:6px">
      <div style="flex:1"><div class="photo-warm" style="height:70px" role="img" aria-label="Service consultant portrait"></div><div class="red" style="height:14px;font-size:5px;color:#fff;display:flex;align-items:center;justify-content:center">Design</div></div>
      <div style="flex:1"><div class="photo-warm" style="height:70px" role="img" aria-label="Service consultant portrait"></div><div class="red" style="height:14px;font-size:5px;color:#fff;display:flex;align-items:center;justify-content:center">Supply</div></div>
      <div style="flex:1"><div class="photo-warm" style="height:70px" role="img" aria-label="Service consultant portrait"></div><div class="red" style="height:14px;font-size:5px;color:#fff;display:flex;align-items:center;justify-content:center">Support</div></div>
    </div>
  </section>

  <!-- 17 building -->
  <section class="slide building">
    <div class="abs photo" style="left:0;top:0;width:100px;height:167px" role="img" aria-label="Skyscraper at dusk"></div>
    <p class="abs title" style="left:112px;top:24px">Lorem ipsum</p>
    <div class="abs red" style="left:112px;top:36px;width:20px;height:2px"></div>
    <p class="abs body" style="left:112px;top:44px;width:98px">Modern plants in major markets.</p>
    <div class="abs" style="left:112px;top:100px;display:flex;gap:14px">
      <span class="icon"></span><span class="icon"></span><span class="icon"></span>
    </div>
  </section>

  <!-- 18 contact -->
  <section class="slide contact">
    <p class="abs title" style="left:0;width:222px;text-align:center;top:12px">Contact us</p>
    <div class="abs" style="left:14px;top:36px;width:110px;height:76px;background:linear-gradient(135deg,#e2e2e2,#c4c4c4)" role="img" aria-label="Map of the United States"></div>
    <div class="abs" style="left:134px;top:42px;display:flex;flex-direction:column;gap:10px;font-size:5px;color:var(--ink)">
      <div style="display:flex;gap:4px;align-items:center">
        <svg width="7" height="9" viewBox="0 0 10 13"><path d="M5 0a5 5 0 0 0-5 5c0 4 5 8 5 8s5-4 5-8a5 5 0 0 0-5-5z" fill="#c8102e"/><circle cx="5" cy="5" r="1.8" fill="#fff"/></svg>
        <span>Dallas, Texas</span></div>
      <div style="display:flex;gap:4px;align-items:center">
        <svg width="7" height="7" viewBox="0 0 10 10"><path d="M2 0l2 2.5-1.2 1.3a6 6 0 0 0 3.4 3.4L7.5 6 10 8 8.5 10C4 10 0 6 0 1.5z" fill="#c8102e"/></svg>
        <span>(555) 014-2200</span></div>
      <div style="display:flex;gap:4px;align-items:center">
        <svg width="8" height="6" viewBox="0 0 10 7"><rect width="10" height="7" fill="#c8102e"/><path d="M0 0l5 4 5-4" stroke="#fff" fill="none" stroke-width=".8"/></svg>
        <span>info@tarrowmead.com</span></div>
    </div>
  </section>

</main>
</body>
</html>
```